Computer business needs new look.

KELD Computers has been selling and repairing, servicing computers in northern NSW for 20 years and has now branched out into Surveillance/ CCTV systems Alarm systems and just about anything technical.
We have also changed our area of operation from just the northern rivers to include all of outback New South Wales and Queensland.
We have changed our name slightly to K.E.L.D Sundown Technical Services.I will include my old business card.The Logo can stay or go i am open to all designs.
Updates

facebook page for info https://www.examplebook.test/pages/KELD-Computers/482019375610283?fref=ts The top half of the business card i uploaded looks pink ! it should be white

I should have mentioned this before. My new look cards will become the look of the business. ie: advertising, vehicle sign-writing etc: The look that i think im after is more to large business/corporate look not "WALLY THE FIXER " Probably the main focus is the fact that we service the small towns in outback Australia. " Billabong Barney " Not just the big city's Please feel free to through any thing at me and any questions please ask.

I have uploaded a picture that i would like the back of the card to look like. Please have a look and see what you can do.

Reason: I am hoping to get some original designs that i like. So far i have just 1 that i like..there must be more ideas out there.

Target Market(s)

Small to medium business

Industry/Entity Type

Business

Contact Information for Business Card

K.E.L.D Sundown Technical Services
Owen Pelkie
1300621745 0457 318206

Requirements
Nice to have
• Back of card to have a list of services
Computer sales
Computer Repairs & Virus removal
Wireless Hotspots
CCTV Installation and repair
Network Design and setup
Troubleshooting

```html
<!DOCTYPE html>
<html lang="en">
<head>
<meta charset="utf-8">
<title>K.E.L.D Sundown Technical Services – Business Card</title>
<link href="https://fonts.googleapis.com/css2?family=Tinos:wght@400;700&family=Arimo:wght@400;700&display=swap" rel="stylesheet">
<style>
  :root {
    --purple: #3a1287;
    --gold: #f5b301;
    --white: #ffffff;
    --ink: #1d1d2b;
    --backdrop: #e6e6ea;
  }
  * { box-sizing: border-box; margin: 0; padding: 0; }
  html, body {
    width: 1200px; height: 884px; overflow: hidden;
    background: var(--backdrop);
  }
  .sheet {
    width: 1200px; height: 884px;
    display: flex; align-items: center; justify-content: center; gap: 60px;
  }
  .card {
    position: relative; width: 520px; height: 297px; overflow: hidden;
    box-shadow: 0 6px 18px rgba(0,0,0,0.18);
  }

  /* Front */
  .card-front { background: var(--white); }
  .front-wave { position: absolute; inset: 0; width: 100%; height: 100%; }
  .brand {
    position: absolute; left: 30px; top: 24px; right: 24px;
    display: flex; align-items: center; gap: 18px;
  }
  .brand-mark {
    width: 64px; height: 64px; border-radius: 50%;
    background: var(--gold); flex: none;
  }
  .brand-name {
    font-family: "Tinos", "Times New Roman", serif; font-weight: 700;
    font-size: 28px; line-height: 1.08; color: var(--purple); letter-spacing: 0.3px;
  }
  .brand-rule {
    position: absolute; left: 30px; right: 22px; top: 104px;
    height: 3px; background: var(--purple);
  }
  .holder {
    position: absolute; right: 24px; top: 114px;
    font-family: "Tinos", "Times New Roman", serif; font-weight: 700;
    font-size: 21px; color: var(--purple);
  }
  .contacts {
    position: absolute; left: 30px; top: 160px;
    display: flex; gap: 22px;
    font-family: "Arimo", Arial, sans-serif; font-size: 13px; color: var(--ink);
    white-space: nowrap;
  }
  .contact { display: flex; align-items: center; gap: 7px; }
  .contact svg { width: 15px; height: 15px; flex: none; }

  /* Back */
  .card-back { background: var(--purple); }
  .services {
    position: absolute; left: 150px; top: 30px; list-style: none;
    font-family: "Arimo", Arial, sans-serif; font-size: 15px; line-height: 22px;
    color: var(--white);
  }
  .services li { display: flex; align-items: center; gap: 10px; }
  .services li::before {
    content: ""; width: 0; height: 0;
    border-left: 5px solid transparent; border-right: 5px solid transparent;
    border-bottom: 8px solid var(--white);
  }
  .web-address {
    position: absolute; left: 215px; top: 196px;
    background: var(--white); color: var(--purple);
    font-family: "Arimo", Arial, sans-serif; font-weight: 700; font-size: 13px;
    padding: 5px 10px;
  }
  .back-stripe {
    position: absolute; left: 0; right: 0; bottom: 10px; height: 9px;
    background: var(--gold);
  }
</style>
</head>
<body>
<main class="sheet">
  <section class="card card-front" aria-label="Business card front">
    <svg class="front-wave" viewBox="0 0 520 297" preserveAspectRatio="none" aria-hidden="true">
      <path d="M0,188 C170,232 350,270 520,290 L520,297 L0,297 Z" fill="var(--gold)"/>
      <path d="M0,200 C170,244 350,280 520,297 L0,297 Z" fill="var(--white)"/>
      <path d="M0,214 C160,252 340,287 520,297 L0,297 Z" fill="var(--purple)"/>
    </svg>
    <div class="brand">
      <span class="brand-mark" aria-hidden="true"></span>
      <h1 class="brand-name">K.E.L.D Sundown<br>Technical Services</h1>
    </div>
    <div class="brand-rule"></div>
    <p class="holder">Owen Pelkie</p>
    <div class="contacts">
      <span class="contact">
        <svg viewBox="0 0 16 16" aria-hidden="true"><path d="M3 1.5 L6 1.5 L7 5 L5.2 6.3 C6 8.3 7.7 10 9.7 10.8 L11 9 L14.5 10 L14.5 13 C14.5 14 13.6 14.6 12.7 14.5 C6.8 13.9 2.1 9.2 1.5 3.3 C1.4 2.4 2 1.5 3 1.5 Z" fill="var(--purple)"/></svg>
        1300 621 745
      </span>
      <span class="contact">
        <svg viewBox="0 0 16 16" aria-hidden="true"><rect x="4" y="1" width="8" height="14" rx="1.5" fill="none" stroke="var(--purple)" stroke-width="1.6"/><circle cx="8" cy="12.5" r="0.9" fill="var(--purple)"/></svg>
        0457 318 206
      </span>
      <span class="contact">
        <svg viewBox="0 0 16 16" aria-hidden="true"><rect x="1" y="3" width="14" height="10" fill="none" stroke="var(--purple)" stroke-width="1.4"/><path d="M1 3 L8 9 L15 3 M1 13 L6 7.5 M15 13 L10 7.5" fill="none" stroke="var(--purple)" stroke-width="1.2"/></svg>
        owen@keldcomputers.test
      </span>
    </div>
  </section>

  <section class="card card-back" aria-label="Business card back">
    <ul class="services">
      <li>Computer sales</li>
      <li>Computer Repairs &amp; Virus removal</li>
      <li>Wireless Hotspots</li>
      <li>CCTV Installation and repair</li>
      <li>Network Design and setup</li>
      <li>Troubleshooting</li>
    </ul>
    <p class="web-address">www.keldcomputers.test</p>
    <div class="back-stripe"></div>
  </section>
</main>
</body>
</html>
```